Tolvane Business Card

I have a business that is called "Brevant Electrical Products LTD" My company deals with top of the range laptops and mobile phones that are exclusive. I need a business card that will be eye catching but not over complicated.

Target Market(s)

Adults aged 19 to 50
Upper middle class

Industry/Entity Type

Business

Requirements
Must have
• Company name/logo (file attached)
• It must have my contact information which is:

• Name: Dale Marwick

• Position: Managing Director 

• Business Address: 7 Hapton Row, London, W4 9QD

• Contact Number: 02085193604
• Mobile: 07814260537
• Email: info@tolvane-goods.co.uk
Nice to have
• Simple and stylish
• Eye catching

```html
<!DOCTYPE html>
<html lang="en">
<head>
<meta charset="utf-8">
<title>Tolvane Electrical Products – Business Card</title>
<link rel="stylesheet" href="https://fonts.googleapis.com/css2?family=Gentium+Book+Plus:wght@400;700&display=swap">
<style>
  :root {
    --stage: #000000;
    --card: #ffffff;
    --cyan: #12f2f7;
    --cyan-strong: #00f6fb;
    --cyan-pale: #b8f7f6;
    --ink: #111111;
    --logo-ink: #1d8fd0;
    --serif: "Gentium Book Plus", Georgia, serif;
  }
  * { margin: 0; padding: 0; box-sizing: border-box; }
  html, body { width: 1200px; height: 1200px; overflow: hidden; background: var(--stage); }
  body { position: relative; font-family: var(--serif); }

  .card {
    position: absolute;
    left: 169px;
    width: 840px;
    height: 480px;
    background: var(--card);
    overflow: hidden;
  }
  .card--front { top: 102px; }
  .card--back { top: 611px; }

  .text { position: absolute; line-height: 1; white-space: nowrap; }

  .logo-block {
    position: absolute;
    background: linear-gradient(to bottom, rgba(184,247,246,0) 35%, var(--cyan-pale) 100%);
  }
  .logo-name {
    position: absolute;
    left: 0; right: 0;
    text-align: center;
    font-size: 34px;
    line-height: 1;
    color: var(--logo-ink);
    letter-spacing: 1px;
  }

  /* front */
  .card--front .logo-block { left: 17px; top: 66px; width: 155px; height: 86px; }
  .card--front .logo-name { top: 8px; }

  .person { position: absolute; left: 520px; width: 300px; top: 46px; text-align: center; }
  .person__name { font-size: 36px; font-weight: 700; color: var(--cyan); line-height: 1.05; }
  .person__role { font-size: 30px; color: var(--ink); line-height: 1.2; margin-top: 1px; }

  .front-company { left: 22px; top: 272px; font-size: 40px; color: var(--cyan); }

  .contact-band {
    position: absolute; left: 0; top: 310px; width: 840px; height: 170px;
    background: linear-gradient(100deg, var(--cyan-strong) 0%, #6ffcfd 40%, #c8fdfd 68%, #ffffff 100%);
  }
  .contact-band__stripe { position: absolute; top: 0; bottom: 0; background: #ffffff; }
  .front-contacts { position: absolute; left: 22px; top: 311px; color: #ffffff; font-size: 30px; line-height: 36px; white-space: nowrap; }

  /* back */
  .card--back .logo-block { left: 342px; top: 141px; width: 182px; height: 95px; }
  .card--back .logo-name { top: 10px; }

  .back-company { left: 0; right: 0; top: 271px; text-align: center; font-size: 40px; color: var(--cyan); }
  .back-rule { position: absolute; left: 0; top: 319px; width: 840px; height: 8px; background: var(--cyan-strong); }
  .back-contacts { position: absolute; left: 246px; top: 338px; color: var(--cyan); font-size: 26px; line-height: 30.5px; white-space: nowrap; }
</style>
</head>
<body>

<section class="card card--front" aria-label="Business card front">
  <div class="logo-block">
    <div class="logo-name">Tolvane</div>
  </div>

  <div class="person">
    <div class="person__name">Dale Marwick</div>
    <div class="person__role">Managing Director</div>
  </div>

  <div class="contact-band">
    <span class="contact-band__stripe" style="left:718px;width:7px"></span>
    <span class="contact-band__stripe" style="left:732px;width:3px"></span>
    <span class="contact-band__stripe" style="left:742px;width:4px"></span>
  </div>

  <div class="text front-company">Tolvane Electrical Products</div>
  <div class="front-contacts">
    <div>7 Hapton Row, London, W4 9QD</div>
    <div>Tel : 02085193604</div>
    <div>Mobile : 07814260537</div>
    <div>Email : info@tolvane-goods.co.uk</div>
  </div>
</section>

<section class="card card--back" aria-label="Business card back">
  <div class="logo-block">
    <div class="logo-name">Tolvane</div>
  </div>

  <div class="text back-company">Tolvane Electrical Products</div>
  <div class="back-rule"></div>
  <div class="back-contacts">
    <div>7 Hapton Row, London, W4 9QD</div>
    <div>Tel : 02085193604</div>
    <div>Mobile : 07814260537</div>
    <div>Email : info@tolvane-goods.co.uk</div>
  </div>
</section>

</body>
</html>
```